Real Estate Agent needs business card design

We have logo designed already, want to have business card designed. Very interested in those smaller size business card as they look very trendy. Business name is called VORENDA REALTY

```html
<!DOCTYPE html>
<html lang="en">
<head>
<meta charset="utf-8">
<title>Vorenda Realty – Business Card</title>
<link href="https://fonts.googleapis.com/css2?family=Open+Sans:wght@400;600;700&display=swap" rel="stylesheet">
<style>
  :root {
    --gold: #c9a36b;
    --gold-light: #e6d2b0;
    --gold-deep: #b89058;
    --ink: #2b241c;
    --text: #222222;
    --white: #ffffff;
    --stage: #3a3a3a;
    --rule: #9a9a9a;
  }
  * { box-sizing: border-box; margin: 0; padding: 0; }
  html, body {
    width: 1200px; height: 831px; overflow: hidden;
    background: var(--stage);
    font-family: "Open Sans", Arial, sans-serif;
  }
  .canvas { position: relative; width: 1200px; height: 831px; }

  .card {
    position: absolute; width: 540px; height: 310px;
    overflow: hidden; box-shadow: 0 10px 28px rgba(0,0,0,.45);
  }

  /* Front */
  .card-front { left: 80px; top: 80px; background: var(--white); }
  .front-wave { position: absolute; left: 0; bottom: 0; width: 540px; height: 310px; }
  .brand-circle {
    position: absolute; left: 62px; top: 42px; width: 176px; height: 176px;
    border-radius: 50%; background: var(--gold);
    display: flex; align-items: center; justify-content: center;
  }
  .brand-name-front {
    color: var(--white); font-weight: 600; font-size: 15px; letter-spacing: 1.5px;
  }
  .divider {
    position: absolute; left: 292px; top: 50px; width: 1px; height: 150px;
    background: var(--rule);
  }
  .divider::before {
    content: ""; position: absolute; left: -1px; top: 0; width: 3px; height: 26px;
    background: var(--gold);
  }
  .contact { position: absolute; left: 312px; top: 46px; color: var(--text); }
  .person-name { color: var(--gold); font-weight: 700; font-size: 19px; line-height: 1.1; }
  .person-title { font-size: 13px; margin-top: 2px; }
  .company { color: var(--gold); font-size: 13px; margin-top: 14px; }
  .address { font-size: 13px; line-height: 1.35; }
  .contact-line { display: flex; align-items: center; gap: 8px; font-size: 13px; margin-top: 4px; }
  .contact-line:first-of-type { margin-top: 6px; }
  .icon { width: 14px; height: 14px; flex: none; }

  /* Back */
  .card-back { left: 580px; top: 440px; background: var(--gold); }
  .world-map {
    position: absolute; left: 40px; top: 20px; width: 460px; height: 250px;
    background: radial-gradient(ellipse at 50% 45%, rgba(184,144,88,.55), rgba(201,163,107,0) 70%);
  }
  .brand-name-back {
    position: absolute; left: 0; right: 0; top: 128px; text-align: center;
    color: var(--ink); font-weight: 600; font-size: 30px; letter-spacing: 3px;
  }
  .back-web {
    position: absolute; left: 0; right: 0; bottom: 34px;
    display: flex; align-items: center; justify-content: center; gap: 14px;
    color: var(--white); font-size: 17px; letter-spacing: 1.5px;
  }
  .back-web::before, .back-web::after {
    content: ""; width: 70px; height: 1px; background: var(--ink);
  }
</style>
</head>
<body>
<main class="canvas">

  <section class="card card-front" aria-label="Business card front">
    <svg class="front-wave" viewBox="0 0 540 310" aria-hidden="true">
      <path d="M0 310 L0 296 C140 282 260 212 540 196 L540 310 Z" fill="var(--gold-light)"/>
      <path d="M0 310 L0 302 C150 292 270 226 540 210 L540 310 Z" fill="var(--white)"/>
      <path d="M0 310 C170 300 290 236 540 218 L540 310 Z" fill="var(--gold)"/>
    </svg>

    <div class="brand-circle"><span class="brand-name-front">VORENDA REALTY</span></div>

    <div class="divider"></div>

    <div class="contact">
      <p class="person-name">Clara Weston</p>
      <p class="person-title">Senior Property Consultant</p>
      <p class="company">Vorenda Realty</p>
      <p class="address">7C, 48 Harbour Road,<br>Eastwood, NSW 2122</p>
      <p class="contact-line">
        <svg class="icon" viewBox="0 0 14 14" aria-hidden="true"><circle cx="7" cy="7" r="7" fill="var(--gold)"/><path d="M4 5.5h6v4H4z M5 4h4v1.5H5z" fill="var(--white)"/></svg>
        0400 517 293
      </p>
      <p class="contact-line">
        <svg class="icon" viewBox="0 0 14 14" aria-hidden="true"><circle cx="7" cy="7" r="7" fill="var(--gold)"/><circle cx="7" cy="7" r="4" fill="none" stroke="var(--white)" stroke-width="1"/><path d="M3 7h8M7 3v8" stroke="var(--white)" stroke-width="1"/></svg>
        www.vorendarealty.com.au
      </p>
    </div>
  </section>

  <section class="card card-back" aria-label="Business card back">
    <div class="world-map" role="img" aria-label="Faint dotted world map in darker gold"></div>
    <p class="brand-name-back">VORENDA REALTY</p>
    <p class="back-web">www.vorendarealty.com.au</p>
  </section>

</main>
</body>
</html>
```